DELVANE ROOFING YARD SIGN

We need a yard sign to put in our customers' yards when we are roofing their home.
Delvane Roofing
468 Pettigrew Rd
Lake Charles LA 70452
phone: 337-555-0148

Maybe some verbiage like "Your Hometown Roofing Experts"
or
"Family Owned Since 1956"

```html
<!DOCTYPE html>
<html lang="en">
<head>
<meta charset="utf-8">
<title>Delvane Roofing Yard Sign</title>
<link href="https://fonts.googleapis.com/css2?family=Poppins:wght@600;700;800&display=swap" rel="stylesheet">
<style>
  :root {
    --page: #ffffff;
    --sign-dark: #141414;
    --sign-dark-2: #262626;
    --ink: #0b0b0b;
    --paper: #f8f8f8;
    --ring: #0a0a0a;
  }
  html, body {
    margin: 0;
    padding: 0;
    width: 1200px;
    height: 901px;
    overflow: hidden;
    background: var(--page);
    font-family: "Poppins", sans-serif;
  }
  .yard-sign {
    position: absolute;
    left: 134px;
    top: 102px;
    width: 940px;
    height: 704px;
    background: var(--paper);
    overflow: hidden;
  }
  .shingle-backdrop {
    position: absolute;
    left: 0;
    top: 0;
    width: 940px;
    height: 626px;
    background: radial-gradient(ellipse at 60% 40%, var(--sign-dark-2), var(--sign-dark) 75%);
  }
  .tagline {
    position: absolute;
    left: 0;
    top: 20px;
    width: 940px;
    text-align: center;
    color: var(--paper);
    font-weight: 700;
    font-size: 26px;
    line-height: 1;
    letter-spacing: 12.5px;
    text-indent: 12px;
    white-space: nowrap;
    margin: 0;
  }
  .ribbon {
    position: absolute;
    top: 233px;
    width: 250px;
    height: 73px;
  }
  .ribbon svg { position: absolute; inset: 0; }
  .ribbon-text {
    position: absolute;
    top: 0;
    height: 73px;
    line-height: 73px;
    font-weight: 700;
    color: var(--ink);
    white-space: nowrap;
  }
  .ribbon-left { left: 25px; }
  .ribbon-left .ribbon-text { left: 45px; font-size: 25px; }
  .ribbon-right { left: 665px; }
  .ribbon-right .ribbon-text { left: 24px; font-size: 30px; top: 2px; }
  .brand-seal {
    position: absolute;
    left: 275px;
    top: 72px;
    width: 392px;
    height: 392px;
  }
  .brand-name {
    position: absolute;
    left: 0;
    top: 0;
    width: 392px;
    height: 392px;
    display: flex;
    align-items: center;
    justify-content: center;
    text-align: center;
    font-weight: 700;
    font-size: 40px;
    line-height: 1.15;
    color: var(--ink);
    margin: 0;
  }
  .phone {
    position: absolute;
    left: 0;
    top: 466px;
    width: 940px;
    text-align: center;
    color: var(--paper);
    font-weight: 800;
    font-size: 124px;
    line-height: 1;
    letter-spacing: -2px;
    white-space: nowrap;
    margin: 0;
  }
  .address {
    position: absolute;
    left: 0;
    top: 630px;
    width: 940px;
    height: 74px;
    line-height: 74px;
    text-align: center;
    color: var(--ink);
    font-weight: 700;
    font-size: 42px;
    letter-spacing: -0.5px;
    white-space: nowrap;
    margin: 0;
  }
</style>
</head>
<body>
  <main class="yard-sign">
    <div class="shingle-backdrop" role="img" aria-label="Dark close-up of asphalt roof shingles"></div>

    <p class="tagline">YOUR HOMETOWN ROOFING EXPERTS</p>

    <div class="ribbon ribbon-left">
      <svg width="250" height="73" viewBox="0 0 250 73" aria-hidden="true">
        <polygon points="0,0 250,0 250,73 0,73 31,36.5" fill="var(--paper)"/>
      </svg>
      <span class="ribbon-text">Family Owned</span>
    </div>

    <div class="ribbon ribbon-right">
      <svg width="250" height="73" viewBox="0 0 250 73" aria-hidden="true">
        <polygon points="0,0 250,0 219,36.5 250,73 0,73" fill="var(--paper)"/>
      </svg>
      <span class="ribbon-text">Since 1956</span>
    </div>

    <div class="brand-seal">
      <svg width="392" height="392" viewBox="0 0 392 392" aria-hidden="true">
        <circle cx="196" cy="196" r="196" fill="var(--ring)"/>
        <circle cx="196" cy="196" r="185" fill="var(--paper)"/>
      </svg>
      <p class="brand-name">Delvane<br>Roofing</p>
    </div>

    <p class="phone">337-555-0148</p>

    <p class="address">468 Pettigrew Rd, Lake Charles LA 70452</p>
  </main>
</body>
</html>
```